Dune Air & Plus business card

I need an awesome, double-sided business card designed with our new logo. I would like the one side black with the colored logo, and the back side is all yours. I'd like to see horizontal and vertical layouts. Get creative! Thank you.

Target Market(s)

HVAC, Heating and Cooling in Phoenix, AZ

Industry/Entity Type

HVAC

Contact Information for Business Card

We need our new logo on the card. Tom Harker, (623) 555-0142, tom@trydunesair.com, www.trydunesair.com, ROC 514273

```html
<!DOCTYPE html>
<html lang="en">
<head>
<meta charset="utf-8">
<title>Dune Air &amp; Plus – Business Card</title>
<link href="https://fonts.googleapis.com/css2?family=Tenor+Sans&display=swap" rel="stylesheet">
<style>
  :root {
    --backdrop: #2e2e2e;
    --card-white: #f7f7f7;
    --ink-black: #050505;
    --text-dark: #1e1e1e;
    --brand-orange: #e4621f;
    --brand-blue: #1f78c4;
    --band-grey: #ececec;
    --url-grey: #333333;
  }
  * { margin: 0; padding: 0; box-sizing: border-box; }
  html, body {
    width: 1200px; height: 900px; overflow: hidden;
    background: var(--backdrop);
    font-family: "Tenor Sans", "Optima", sans-serif;
  }
  .stage {
    width: 1200px; height: 900px;
    display: flex; align-items: center; justify-content: center; gap: 70px;
  }
  .card {
    position: relative;
    width: 340px; height: 595px;
    box-shadow: 0 18px 40px rgba(0,0,0,0.45);
    overflow: hidden;
  }

  /* Front */
  .card--front { background: var(--card-white); }
  .card__edge-stripe {
    position: absolute; top: 0; bottom: 0; left: 14px; width: 32px;
    background: var(--ink-black);
  }
  .brand {
    position: absolute; left: 46px; right: 0; top: 72px;
    display: flex; align-items: center; justify-content: center; gap: 10px;
  }
  .brand__dot {
    width: 16px; height: 16px; border-radius: 50%;
    background: var(--brand-orange);
  }
  .brand__name {
    font-size: 27px; color: var(--brand-blue); letter-spacing: 0.5px;
  }
  .contact {
    position: absolute; left: 86px; top: 392px;
    color: var(--text-dark);
  }
  .contact__name {
    font-size: 25px; color: var(--brand-orange);
    text-transform: uppercase; letter-spacing: 0.5px;
    margin-bottom: 14px;
  }
  .contact__list { list-style: none; }
  .contact__item {
    display: flex; align-items: center; gap: 10px;
    font-size: 17px; line-height: 1; margin-bottom: 13px;
  }
  .contact__icon { width: 16px; height: 16px; flex: none; }
  .contact__licence {
    margin-top: 6px; font-size: 21px; color: var(--brand-blue);
    letter-spacing: 1.5px;
  }

  /* Back */
  .card--back { background: var(--ink-black); }
  .card--back .brand { left: 0; top: 228px; }
  .card--back .brand__name { font-size: 30px; }
  .back__band {
    position: absolute; left: 0; right: 0; top: 470px; height: 44px;
    background: var(--band-grey);
    display: flex; align-items: center; justify-content: center;
    font-size: 17px; color: var(--url-grey); letter-spacing: 1.5px;
  }
</style>
</head>
<body>
<main class="stage">

  <section class="card card--front" aria-label="Business card front">
    <div class="card__edge-stripe"></div>
    <div class="brand">
      <span class="brand__dot"></span>
      <span class="brand__name">Dune Air &amp; Plus</span>
    </div>
    <div class="contact">
      <h1 class="contact__name">Tom Harker</h1>
      <ul class="contact__list">
        <li class="contact__item">
          <svg class="contact__icon" viewBox="0 0 24 24" aria-hidden="true"><path fill="#1f78c4" d="M6.6 10.8a15.1 15.1 0 0 0 6.6 6.6l2.2-2.2a1 1 0 0 1 1-.25 11.4 11.4 0 0 0 3.6.57 1 1 0 0 1 1 1V20a1 1 0 0 1-1 1A17 17 0 0 1 3 4a1 1 0 0 1 1-1h3.5a1 1 0 0 1 1 1c0 1.25.2 2.45.57 3.6a1 1 0 0 1-.25 1z"/></svg>
          (623) 555-0142
        </li>
        <li class="contact__item">
          <svg class="contact__icon" viewBox="0 0 24 24" aria-hidden="true"><rect x="2" y="5" width="20" height="14" rx="2" fill="#1f78c4"/><path d="M3 6l9 7 9-7" fill="none" stroke="#fff" stroke-width="1.6"/></svg>
          tom@trydunesair.com
        </li>
        <li class="contact__item">
          <svg class="contact__icon" viewBox="0 0 24 24" aria-hidden="true"><circle cx="12" cy="12" r="10" fill="#1f78c4"/><path d="M2 12h20M12 2c3 3 3 17 0 20M12 2c-3 3-3 17 0 20" fill="none" stroke="#fff" stroke-width="1.2"/></svg>
          www.trydunesair.com
        </li>
      </ul>
      <p class="contact__licence">ROC 514273</p>
    </div>
  </section>

  <section class="card card--back" aria-label="Business card back">
    <div class="brand">
      <span class="brand__dot"></span>
      <span class="brand__name">Dune Air &amp; Plus</span>
    </div>
    <div class="back__band">www.trydunesair.com</div>
  </section>

</main>
</body>
</html>
```